依頼詳細
店内は和風でホームページも癒しの雰囲気で作っておりますが、100%きれいな画像で癒しだけの雰囲気だとほかのお店との差別化ができない為、当店は技術もすごいというような雰囲気もホームページにも少し出してアピール度を増したホームページにしたいと考えております。
ホームページに加え、今回依頼する背景画像のデザインはロゴやアピールしたい言葉を入れ、刷り込み効果+ファーストインプレッションでひきつけ度をアップさせたいです。
あくまで背景なので目立ちすぎないように。
記載項目
●入れて欲しい単語(参考データ添付)
「安心安全」「すご腕集団」「評判の人気店」「予約殺到中」「選ばれている」「口コミ全国1位」「極上癒し」「肩こり」「腰痛」「疲れ」「最大規模」「達人の技」「御用達」「圧倒的」「プロ集団」「職人の技」「ストレッチ」「ほぐし整体」「アロマオイル」「人気NO1」「ご褒美」「新宿駅近」
●ロゴを入れて欲しい(データー添付)
●ほぐし技のイラスト集を入れて欲しい(データ添付/色を変える)
以上の、単語とイラストとロゴをうまく組み合わせて背景を創って欲しい。
希望イメージ
シンプル 複雑
単色 カラフル
暗い 明るい
日常 高級
遊び心 厳粛
未来的 伝統的
女性的 男性的
希望する色
黒、グレー、薄めの暖色系
納品ファイル
• 高解像度JPG (.jpg)
• イラストレーター形式 (.ai)
• フォトショップ形式 (.psd)
• PNG形式 (.png)
補足説明
現在制作中のホームページのアドレスを送りますので、バランスを見て制作して頂きアップする時はホームページと背景が両方映ったもので見たいです。
制作中のホームページ
http://pelmoritz.com/sample-beauty/
ホームページの本体のバックは左右の切れ端が一番大きな画像から2cmぐらいで切ろうかと思っておりますので、その左右の先が背景画像にしたいと考えてます。
ただ、全体を背景画像で埋めるより、下の方に行けば自然と薄くなって消えていくとか、背景画像自体に丸みがあるとか、外側の輪郭も工夫して頂けると面白いかと思います。
色は2色、多くても3色まででお願いいたします。
あくまで背景ですので目立ちすぎず、しかしながら自然と目に留まりアピールできるような~
感じでお願いいたします。
※添付の背景画像のサンプルはCの部分に2種類ほど単語があるかと思いますので、そちらを参考イメージにロゴとイラストを追加してお願いいたします。
※イラストに関しては添付データから24種類あるかと思いますが、できるだけ違うイラストを使い
工夫してみてください。
急ぎで申し訳ございませんがよろしくお願いいたします。
あなたのご協力をお待ちしております。
参考データを送ります。
http://www.kohaku-sorane.jp/

参考データのものは白い部分が多すぎですが、グラデーションを使って白い部分のラインを工夫して頂けると面白いかと思います。

急募にもかかわらず迅速にご対応してくれました。

今回、少し指示が曖昧で伝わりにくかった中で皆さんご対応が的確で、どの方もデザインが素晴らしかったです。
また、次回もお願いいたします。

新宿 くつろぎ庵

```html
<!DOCTYPE html>
<html lang="ja">
<head>
<meta charset="utf-8">
<title>新宿 ゆるり亭</title>
<link href="https://fonts.googleapis.com/css2?family=Noto+Sans+JP:wght@400;700;900&family=Noto+Serif+JP:wght@700;900&display=swap" rel="stylesheet">
<style>
:root{
  --brown:#5a3519;
  --brown-2:#8a5a2b;
  --orange:#e8891e;
  --cream:#f6eedf;
  --beige:#e9dcc2;
  --plum:#8d4b78;
  --rose:#c98aa8;
  --red:#c4302b;
  --white:#fff;
}
*{margin:0;padding:0;box-sizing:border-box}
html,body{width:732px;height:1200px;overflow:hidden;background:var(--white)}
body{font-family:"Noto Sans JP",sans-serif;color:#333;font-size:8px;line-height:1.35}
.canvas{position:relative;width:732px;height:1200px;overflow:hidden;background:var(--white)}

.side{position:absolute;top:0;width:86px;height:1200px;
  background:linear-gradient(180deg,#8c8c8c 0%,#bdbdbd 35%,#e6e6e6 70%,#fff 100%)}
.side.left{left:0;border-radius:0 60px 60px 0}
.side.right{right:0;border-radius:60px 0 0 60px}
.side .word{position:absolute;writing-mode:vertical-rl;font-family:"Noto Serif JP",serif;font-weight:900;color:rgba(255,255,255,.8);letter-spacing:2px;line-height:1}
.side .word.dark{color:rgba(60,60,60,.55)}
.side .art{position:absolute;border-radius:50%;background:radial-gradient(circle,#9a9a9a,#c8c8c8)}

.page{position:absolute;left:86px;top:0;width:560px;height:1200px;background:var(--white)}
.topline{height:12px;background:var(--cream);font-size:6px;color:var(--brown);padding:2px 6px;display:flex;justify-content:space-between}
.header{height:90px;display:flex;align-items:center;padding:0 8px;border-bottom:2px solid var(--beige)}
.brand{display:flex;align-items:center;gap:6px;width:150px}
.brand-mark{width:22px;height:22px;border-radius:50%;background:var(--orange)}
.brand-name{font-family:"Noto Serif JP",serif;font-weight:900;font-size:17px;color:var(--brown)}
.tagline{flex:1;font-size:8px;color:var(--brown);font-weight:700;text-align:center}
.tagline span{display:block;font-size:7px;font-weight:400;color:#666}
.contact{width:150px;text-align:right;color:var(--brown)}
.contact .tel{font-size:17px;font-weight:900;color:var(--orange);display:flex;align-items:center;justify-content:flex-end;gap:3px}
.contact small{display:block;font-size:6.5px}
.nav{height:35px;display:flex;gap:2px;padding:2px 0;background:var(--cream)}
.nav a{flex:1;background:linear-gradient(var(--brown-2),var(--brown));color:#fff;font-size:7.5px;font-weight:700;text-decoration:none;display:flex;align-items:center;justify-content:center;border-radius:3px 3px 0 0;text-align:center}
.hero{margin-top:5px;height:175px;position:relative;background:linear-gradient(90deg,#e7c4cf,var(--rose) 40%,var(--plum) 75%,#5e2d4c)}
.hero p{position:absolute;right:14px;top:60px;color:#fff;font-family:"Noto Serif JP",serif;font-weight:700;font-size:11px;line-height:1.7;text-align:center}

.body{display:flex;gap:6px;margin-top:6px;padding:0 2px}
.sidebar{width:138px}
.main{flex:1}

.box{border:1px solid var(--beige);background:var(--cream);margin-bottom:6px;padding:5px}
.box h3{font-size:8px;color:#fff;background:var(--brown);padding:2px 4px;margin:-5px -5px 4px}
.bookbtn{height:38px;background:linear-gradient(var(--orange),#c96c10);color:#fff;font-weight:900;font-size:10px;display:flex;align-items:center;justify-content:center;border-radius:4px;margin-bottom:6px}
.telbox{text-align:center;color:var(--brown)}
.telbox strong{display:block;font-size:15px;color:var(--red);font-weight:900}
.menu li{list-style:none;border-bottom:1px dotted var(--brown-2);padding:2px 0 2px 8px;font-size:7px;position:relative}
.menu li::before{content:"";position:absolute;left:1px;top:5px;border:3px solid transparent;border-left-color:var(--orange)}
.collage{height:400px;background:linear-gradient(180deg,#c79a78,#8a5a3b 50%,#d8b89a)}
.aside-note{height:100px;background:var(--cream);border:1px solid var(--beige);margin-top:6px;padding:5px;font-size:7px}

.strip{height:36px;border:1px solid var(--beige);display:flex;align-items:center;justify-content:center;font-size:8px;color:var(--brown);font-weight:700;margin-bottom:4px}
.photos{display:flex;gap:4px;margin-bottom:8px}
.photos .ph{flex:1;height:48px;background:linear-gradient(#d7b59a,#a06f4c)}
.badges{display:flex;gap:6px;margin-bottom:8px}
.badge{flex:1;height:70px;border:1px solid var(--beige);background:var(--cream);display:flex;align-items:center;justify-content:center;font-size:7px;color:var(--brown);font-weight:700;text-align:center;gap:4px}
.badge .disc{width:30px;height:30px;border-radius:50%;background:var(--orange)}
.badge.coupon{background:var(--red);color:#fff;font-size:11px}
.twins{display:flex;gap:6px;margin-bottom:8px}
.twin{flex:1}
.twin h4{background:var(--beige);color:var(--brown);font-size:7.5px;padding:3px 5px}
.twin p{font-size:6.5px;padding:3px 4px;height:28px}
.twin .ph{height:52px;background:linear-gradient(#a0522d,#6b3420)}
.twin .ph + .ph{margin-left:2px}
.row2{display:flex}
.row2 .ph{flex:1}
.news{display:flex;gap:6px;margin-bottom:8px}
.news .box{flex:1;height:130px;background:#fff}
.news li{list-style:none;font-size:6.5px;border-bottom:1px dotted #bbb;padding:2px 0}
.news li b{color:var(--orange);font-weight:700;margin-right:3px}
.gallery{border:1px solid var(--beige);padding:0 5px 5px}
.gallery h3{font-size:8px;color:#fff;background:var(--brown);padding:2px 4px;margin:0 -5px 6px}
.grid{display:grid;grid-template-columns:1fr 1fr;gap:8px 10px}
.grid figure{text-align:center;font-size:6.5px}
.grid .ph{height:62px;background:linear-gradient(#b34a3a,#6e2a20);margin-bottom:2px}
.footer{position:absolute;left:0;right:0;bottom:0;height:86px;background:var(--brown);color:#f3e5cc;font-size:7px;padding:10px;text-align:center}
.footer b{display:block;font-size:11px;margin-bottom:4px}
</style>
</head>
<body>
<div class="canvas">

  <div class="side left">
    <div class="art" style="left:10px;top:40px;width:60px;height:60px" role="img" aria-label="ほぐし技のイラスト"></div>
    <span class="word" style="left:33px;top:120px;font-size:20px">予約殺到中</span>
    <span class="word dark" style="left:8px;top:232px;font-size:14px">極上癒し</span>
    <div class="art" style="left:12px;top:330px;width:56px;height:56px" role="img" aria-label="肩もみのイラスト"></div>
    <span class="word" style="left:34px;top:400px;font-size:18px">すご腕集団</span>
    <span class="word dark" style="left:10px;top:520px;font-size:13px">達人の技</span>
    <div class="art" style="left:14px;top:610px;width:52px;height:52px;opacity:.6" role="img" aria-label="ストレッチのイラスト"></div>
    <span class="word" style="left:33px;top:690px;font-size:15px">新宿駅近</span>
  </div>

  <div class="side right">
    <span class="word" style="left:34px;top:30px;font-size:18px">口コミ全国1位</span>
    <div class="art" style="left:16px;top:190px;width:58px;height:58px" role="img" aria-label="腰ほぐしのイラスト"></div>
    <span class="word" style="left:22px;top:270px;font-size:20px">職人の技</span>
    <span class="word dark" style="left:56px;top:270px;font-size:12px">人気NO1</span>
    <div class="art" style="left:14px;top:430px;width:56px;height:56px" role="img" aria-label="アロマオイル施術のイラスト"></div>
    <span class="word" style="left:34px;top:510px;font-size:16px">プロ集団</span>
    <span class="word dark" style="left:10px;top:610px;font-size:12px">ご褒美</span>
  </div>

  <div class="page">
    <div class="topline"><span>新宿の整体・マッサージなら駅近の癒し処</span><span>ご予約はお電話でどうぞ</span></div>

    <header class="header">
      <div class="brand"><span class="brand-mark"></span><span class="brand-name">ゆるり亭</span></div>
      <div class="tagline">新宿駅から徒歩3分 ほぐし整体の専門店<span>肩こり・腰痛・疲れをじっくり解消します</span></div>
      <div class="contact">
        <small>ご予約・お問い合わせ</small>
        <div class="tel"><svg width="12" height="12" viewBox="0 0 24 24"><path fill="#e8891e" d="M6.6 10.8a15 15 0 006.6 6.6l2.2-2.2a1 1 0 011-.25 11 11 0 003.6.6 1 1 0 011 1V20a1 1 0 01-1 1A17 17 0 013 4a1 1 0 011-1h3.5a1 1 0 011 1 11 11 0 00.6 3.6 1 1 0 01-.25 1z"/></svg>03-5210-4477</div>
        <small>営業 11:00〜翌5:00 年中無休</small>
      </div>
    </header>

    <nav class="nav">
      <a>トップ</a><a>ゆるり亭の<br>こだわり</a><a>料金<br>メニュー</a><a>初めての方へ</a><a>スタッフ<br>紹介</a><a>アクセス</a><a>求人情報</a>
    </nav>

    <div class="hero" role="img" aria-label="和室で施術を受ける女性と施術師の写真">
      <p>やはり実績が違います。<br>年間延べ3万人以上の実績！</p>
    </div>

    <div class="body">
      <aside class="sidebar">
        <div class="bookbtn">オンライン予約</div>
        <div class="box telbox"><h3>お電話でのご予約</h3>当日予約も大歓迎<strong>03-5210-4477</strong>受付 11:00〜翌5:00</div>
        <div class="box">
          <h3>Menu</h3>
          <ul class="menu">
            <li>ほぐし整体コース</li><li>アロマオイルコース</li><li>ストレッチコース</li><li>足つぼコース</li><li>ヘッドスパ</li><li>延長・オプション</li><li>回数券のご案内</li>
          </ul>
        </div>
        <div class="collage" role="img" aria-label="マッサージ施術の写真集"></div>
        <div class="aside-note">店舗情報<br>新宿区西新宿1丁目<br>駅から徒歩3分の好立地</div>
      </aside>

      <main class="main">
        <div class="strip">こんなサラリーマンの方に選ばれています</div>
        <div class="photos">
          <div class="ph" role="img" aria-label="施術風景の写真"></div>
          <div class="ph" role="img" aria-label="施術風景の写真"></div>
          <div class="ph" role="img" aria-label="施術風景の写真"></div>
        </div>
        <div class="badges">
          <div class="badge"><span class="disc"></span>口コミ<br>全国1位</div>
          <div class="badge">新宿駅近<br>年中無休で営業</div>
          <div class="badge coupon">Coupon</div>
        </div>
        <div class="twins">
          <div class="twin">
            <h4>ほぐし整体ができるまで</h4>
            <p>一人ひとりの体に合わせた施術で、深いコリまでしっかりほぐします。</p>
            <div class="row2"><div class="ph" role="img" aria-label="店内の写真"></div><div class="ph" role="img" aria-label="店内の写真"></div></div>
          </div>
          <div class="twin">
            <h4>初めての方も安心して</h4>
            <p>丁寧なカウンセリングで、ご希望の強さや部位をお伺いします。</p>
            <div class="row2"><div class="ph" role="img" aria-label="個室の写真"></div><div class="ph" role="img" aria-label="個室の写真"></div></div>
          </div>
        </div>
        <div class="news">
          <div class="box"><h3>Information</h3><ul><li><b>2013.12.01</b>年末年始の営業</li><li><b>2013.11.20</b>新メニュー登場</li><li><b>2013.11.05</b>求人のお知らせ</li></ul></div>
          <div class="box"><h3>Blog</h3><ul><li><b>2013.12.03</b>冬の肩こり対策</li><li><b>2013.11.28</b>スタッフ日記</li></ul></div>
        </div>
        <section class="gallery">
          <h3>フォトギャラリー</h3>
          <div class="grid">
            <figure><div class="ph" role="img" aria-label="施術室の写真"></div>施術室A</figure>
            <figure><div class="ph" role="img" aria-label="施術室の写真"></div>施術室B</figure>
            <figure><div class="ph" role="img" aria-label="待合室の写真"></div>待合室</figure>
            <figure><div class="ph" role="img" aria-label="受付の写真"></div>受付</figure>
          </div>
        </section>
      </main>
    </div>

    <footer class="footer"><b>新宿 ゆるり亭</b>東京都新宿区西新宿1丁目 ／ TEL 03-5210-4477<br>Copyright 新宿 ゆるり亭 All Rights Reserved.</footer>
  </div>
</div>
</body>
</html>
```